Book Cover: A Quiet Cartographer

DO NOT JUST COPY THE BOOK COVER I HAVE ADDED FOR REFERENCE. I NEED SOMETHING FRESH NOT JUST A COPY AND PASTE!
If you cannot improve on the design with something creative then don't submit a design.

Project Title:
Book Cover Design for A Quiet Cartographer

Must be better than the mock design I have uploaded in project files.

Project Description:
I’m looking for a striking and emotionally evocative book cover for my upcoming title A Quiet Cartographer. This is a deeply personal and powerful memoir about the masks we wear, emotional survival, control, and the journey toward radical self-awareness and healing. The cover should visually represent the contrast between the performative self and the authentic self.

Visual Concept:
Please take visual inspiration and design continuity from my previous book Run FAR Now! — I will upload that cover for reference. This new design should feel like a continuation of the same author journey, but bolder and more psychologically intense.

You’ll be provided with two photos of me:

One where I appear more unkept, raw, and emotionally heavy.

One where I appear clean, centered, and lighter.

These can either be:

Split down the middle to create a “mirror” or duality effect (symbolizing the split self),

Or placed side by side as a subtle before/after or internal/external representation.

You may also consider overlaying or fading one into the other if done tastefully.

The mood should hint at internal conflict, self-reckoning, and healing—but without looking too “self-help cliché.” Think masculine, introspective, modern, and editorial. Avoid overly bright or busy visuals. A minimal or clean design with strong type hierarchy is preferred.

Key Themes to Represent Visually (even abstractly):

Narcissism as a survival mechanism

The emotional cost of performance

The tension between image and authenticity

The healing journey from ego to empathy

Design References:

Run FAR Now! (uploaded) — continuity of brand and typography encouraged

Memoir-style covers like Lanterns Along the Winter Harbour, Saltwater, or A Kettle Hums at Dusk for layout feel

If using color, muted tones with contrast (black/white, sepia, desaturated blues or greys) work well

Title: A Quiet Cartographer
Subtitle (optional placement): Not every narcissist is a monster. Some are just wounded men trying their best to survive
Author: Marlon Weskett

Deliverables:

Full front cover for print sale size as previous cover, including space for subtitle and author name

Spine and back cover (leave placeholder text if no blurb is given)

Ebook cover version

High-resolution files suitable for Quillmark QPS and print use

Additional Notes:
Please ensure the tone stays emotionally resonant, masculine, and sophisticated. No stock image models or cliché therapist symbols. Use my uploaded photos only.

Looking forward to seeing your vision come to life.

Back Cover Blurb – A Quiet Cartographer
A brutally honest recovery story—about what happens after you get clean, and the ego you still have to face.
Most people think addiction ends when you put down the drink, the drug, or the chaos.
But for Marlon Weskett, sobriety was just the start.
Behind the personal development posts, six-pack selfies, and billion-rand property deals, he was still chasing the one thing rehab never took from him: the need to be admired.
This book is not a confession. It’s a dismantling.
In A Quiet Cartographer, Marlon exposes the hidden patterns of ego, control, and validation-seeking that nearly cost him everything—even after he got “better.” With fearless self-inquiry and raw storytelling, he invites readers into his recovery from performance, perfectionism, and power addiction.
Whether you’ve been the narcissist—or you’ve loved one—this book is a mirror. And what you’ll find is not just insight, but a new path forward: one where truth is more powerful than charm, and safety matters more than being impressive.
This isn’t about being perfect.
It’s about being honest.
And finally becoming someone worth trusting—especially by yourself.

Target Market(s)

Any reader wanting to read about narcissism and love

Font styles to use
Sans Serif

Colors
EB3D1F
EC4F4E
F09395
F8D3D4
FCEDEE

Requirements
Must have
• Must be better than the mock design I uploaded.

```html
<!DOCTYPE html>
<html lang="en">
<head>
<meta charset="utf-8">
<title>A Quiet Cartographer — Marlon Weskett</title>
<link rel="stylesheet" href="https://fonts.googleapis.com/css2?family=Bebas+Neue&family=Montserrat:wght@300;400;500&family=Oswald:wght@300&display=swap">
<style>
  :root {
    --ground: #1b1a1c;
    --ground-edge: #0f0e10;
    --accent: #eb3d1f;
    --accent-soft: #ec4f4e;
    --blush: #f09395;
    --pale: #f8d3d4;
    --paper: #fcedee;
    --raw-dark: #2e2926;
    --raw-mid: #6b5d55;
    --clean-mid: #9a979a;
    --clean-light: #d6d3d4;
  }
  html, body {
    margin: 0;
    padding: 0;
    width: 846px;
    height: 1200px;
    overflow: hidden;
    background: var(--ground);
  }
  .cover { display: block; width: 846px; height: 1200px; }
  .endorsement {
    font-family: "Montserrat", sans-serif;
    font-weight: 300;
    font-size: 18px;
    fill: var(--paper);
  }
  .endorsement-name { fill: var(--blush); font-weight: 500; letter-spacing: 2px; }
  .title-kicker {
    font-family: "Oswald", sans-serif;
    font-weight: 300;
    font-size: 36px;
    letter-spacing: 18px;
    fill: var(--pale);
  }
  .title-main {
    font-family: "Bebas Neue", sans-serif;
    font-size: 132px;
    fill: var(--paper);
  }
  .subtitle {
    font-family: "Montserrat", sans-serif;
    font-weight: 300;
    font-size: 19px;
    fill: var(--pale);
  }
  .subtitle-lead { font-weight: 500; fill: var(--paper); }
  .author {
    font-family: "Bebas Neue", sans-serif;
    font-size: 50px;
    letter-spacing: 14px;
    fill: var(--paper);
  }
</style>
</head>
<body>
<svg class="cover" viewBox="0 0 846 1200" xmlns="http://www.w3.org/2000/svg">
  <defs>
    <radialGradient id="ground" cx="0.5" cy="0.38" r="0.8">
      <stop offset="0" stop-color="#2a282b"/>
      <stop offset="1" stop-color="var(--ground-edge)"/>
    </radialGradient>
    <linearGradient id="raw-half" x1="0" y1="0" x2="1" y2="1">
      <stop offset="0" stop-color="var(--raw-dark)"/>
      <stop offset="1" stop-color="var(--raw-mid)"/>
    </linearGradient>
    <linearGradient id="clean-half" x1="1" y1="0" x2="0" y2="1">
      <stop offset="0" stop-color="var(--clean-light)"/>
      <stop offset="1" stop-color="var(--clean-mid)"/>
    </linearGradient>
    <linearGradient id="portrait-fade" x1="0" y1="0" x2="0" y2="1">
      <stop offset="0.7" stop-color="var(--ground)" stop-opacity="0"/>
      <stop offset="1" stop-color="var(--ground)" stop-opacity="0.9"/>
    </linearGradient>
  </defs>

  <rect class="backdrop" width="846" height="1200" fill="url(#ground)"/>

  <text class="endorsement" text-anchor="middle">
    <tspan x="423" y="58">“Whatever we’ve been through, Marlon not only</tspan>
    <tspan x="423" y="84">makes us feel we can get over it, he gives us</tspan>
    <tspan x="423" y="110">the tools to do exactly that.” <tspan class="endorsement-name">PETER LINDQVAR</tspan></tspan>
  </text>

  <g class="portrait" role="img" aria-label="Split portrait of the author: left half raw and heavy in warm sepia shadow, right half clean and lighter in soft grey">
    <rect class="portrait-raw" x="173" y="150" width="250" height="620" fill="url(#raw-half)"/>
    <rect class="portrait-clean" x="423" y="150" width="250" height="620" fill="url(#clean-half)"/>
    <rect class="portrait-fade" x="173" y="150" width="500" height="620" fill="url(#portrait-fade)"/>
  </g>
  <rect class="split-line" x="422" y="132" width="2" height="656" fill="var(--accent)"/>

  <text class="title-kicker" x="432" y="836" text-anchor="middle">A QUIET</text>
  <text class="title-main" x="83" y="968" textLength="680" lengthAdjust="spacingAndGlyphs">CARTOGRAPHER</text>

  <rect class="title-rule" x="383" y="996" width="80" height="3" fill="var(--accent-soft)"/>

  <text class="subtitle" text-anchor="middle">
    <tspan class="subtitle-lead" x="423" y="1038">Not every narcissist is a monster.</tspan>
    <tspan x="423" y="1066">Some are just wounded men trying their best to survive.</tspan>
  </text>

  <text class="author" x="430" y="1152" text-anchor="middle">MARLON WESKETT</text>
</svg>
</body>
</html>
```